Town Planning Consultants require lstationary design

Require a design to be used for our letterhead and report cover page. We have an approved logo.
we have attached our logo, and our temporary letterhead/cover page (SEE Cover) which we currently adapt for both purposes in the interim pending a permanent design. I have also attached an example (example report cover) of a report cover page that I like. perhaps similar with our colour scheme

Target Market(s)

?

Industry/Entity Type

Town

Colors
249fd4
3176b5

Requirements
Must have
• colours to match logo
• the text content in existing letterhead

```html
<!DOCTYPE html>
<html lang="en">
<head>
<meta charset="utf-8">
<title>Marlow Urban – Report Cover and Letterhead</title>
<link href="https://fonts.googleapis.com/css2?family=Montserrat:wght@400;500;600&family=Michroma&family=Open+Sans:wght@400;600&display=swap" rel="stylesheet">
<style>
  :root {
    --brand-blue: #24a5d9;
    --brand-blue-deep: #3176b5;
    --wave-grey: #9a9a9a;
    --ink-grey: #8a8a8a;
    --text-grey: #6d6d6d;
    --paper: #ffffff;
    --backdrop: #e4e6e8;
  }
  * { box-sizing: border-box; margin: 0; padding: 0; }
  html, body { width: 1200px; height: 922px; overflow: hidden; }
  body {
    background: var(--backdrop);
    font-family: "Montserrat", Arial, sans-serif;
    position: relative;
  }
  .sheet {
    position: absolute;
    top: 120px;
    width: 526px;
    height: 680px;
    background: var(--paper);
    box-shadow: 6px 8px 14px rgba(0,0,0,0.28);
    overflow: hidden;
  }
  .report-cover { left: 43px; }
  .letterhead { left: 632px; }

  /* Report cover */
  .cover-wave { position: absolute; inset: 0; width: 100%; height: 100%; }
  .brand-name {
    position: absolute;
    font-weight: 500;
    color: var(--brand-blue);
    white-space: nowrap;
    display: flex;
    align-items: center;
  }
  .brand-mark {
    display: inline-block;
    background: var(--brand-blue);
  }
  .report-cover .brand-name { right: 30px; top: 80px; font-size: 40px; gap: 12px; }
  .report-cover .brand-mark { width: 26px; height: 26px; }
  .doc-type {
    position: absolute; right: 30px; top: 176px;
    font-family: "Michroma", sans-serif;
    font-size: 14px; color: var(--brand-blue); letter-spacing: 0.3px;
  }
  .doc-title {
    position: absolute; right: 30px; top: 230px;
    text-align: right; font-size: 24px; line-height: 30px;
    font-weight: 500; color: var(--brand-blue);
  }
  .council-name {
    position: absolute; left: 31px; top: 448px;
    font-size: 28px; font-weight: 400; color: var(--paper); letter-spacing: 0.3px;
  }
  .site-address {
    position: absolute; left: 31px; top: 533px; width: 470px;
    font-family: "Open Sans", Arial, sans-serif;
    font-size: 12px; font-weight: 600; color: var(--paper); line-height: 17px;
  }
  .site-address .line-two { font-size: 10.5px; }
  .proposal {
    position: absolute; left: 31px; top: 576px;
    font-size: 10.3px; color: var(--paper);
  }
  .issue-date {
    position: absolute; left: 411px; top: 633px;
    width: 85px; height: 22px;
    border: 1px solid var(--paper);
    color: var(--paper); font-size: 9.5px;
    display: flex; align-items: center; justify-content: center;
  }
  .issue-date sup { font-size: 6px; }

  /* Letterhead */
  .letterhead .brand-name { left: 22px; top: 48px; font-size: 34px; gap: 10px; }
  .letterhead .brand-mark { width: 22px; height: 22px; }
  .contact-list {
    position: absolute; right: 20px; top: 49px;
    list-style: none; text-align: right;
    font-size: 11.5px; line-height: 13.6px; color: var(--text-grey);
  }
  .contact-list li { display: flex; align-items: center; justify-content: flex-end; gap: 8px; }
  .contact-list svg { width: 9px; height: 9px; fill: var(--brand-blue); }
  .header-rule {
    position: absolute; left: 0; right: 0; top: 110px;
    height: 1px; background: var(--brand-blue);
  }
  .footer-address {
    position: absolute; left: 0; right: 0; top: 650px;
    display: flex; align-items: center; gap: 6px;
    font-size: 11.5px; color: var(--text-grey); white-space: nowrap;
  }
  .footer-address::before, .footer-address::after {
    content: ""; flex: 1; height: 1px; background: var(--brand-blue);
  }
</style>
</head>
<body>

<section class="sheet report-cover">
  <svg class="cover-wave" viewBox="0 0 619 800" preserveAspectRatio="none" aria-hidden="true">
    <path d="M0,72 C40,240 160,350 310,392 C465,436 575,540 619,705 L619,800 L0,800 Z" fill="var(--wave-grey)"/>
    <path d="M0,95 C60,290 190,375 320,418 C470,468 575,565 619,715 L619,800 L0,800 Z" fill="var(--brand-blue)"/>
    <path d="M0,72 C40,240 160,350 310,392 C465,436 575,540 619,705" fill="none" stroke="var(--brand-blue)" stroke-width="1.5"/>
  </svg>

  <div class="brand-name"><span class="brand-mark"></span>Marlow Urban</div>
  <p class="doc-type">DEVELOPMENT APPLICATION</p>
  <h1 class="doc-title">Statement of<br>Environmental Effects</h1>

  <h2 class="council-name">The Ridgefield Shire Council</h2>
  <p class="site-address">LOT 3 DP 418592 &amp; Lot 9 DP57314 No 612 Old Ferris Road &amp; No 7 Quarry Lane<br><span class="line-two">Road, ELMSTEAD</span></p>
  <p class="proposal">Redevelopment of an Existing Shopping Centre in 2 Stages for “Shop top Housing”.</p>
  <p class="issue-date">25<sup>TH</sup>&nbsp;JULY, 2016</p>
</section>

<section class="sheet letterhead">
  <div class="brand-name"><span class="brand-mark"></span>Marlow Urban</div>
  <ul class="contact-list">
    <li>+347 7814-2093
      <svg viewBox="0 0 10 10" aria-label="phone"><path d="M2,0.5 L3.6,0.5 L4.2,2.8 L3.1,3.6 C3.6,4.9 5,6.4 6.4,6.9 L7.2,5.8 L9.5,6.4 L9.5,8 C9.5,9 8.6,9.6 7.6,9.4 C4.2,8.6 1.4,5.8 0.6,2.4 C0.4,1.4 1,0.5 2,0.5 Z"/></svg></li>
    <li>+347 5172-6640
      <svg viewBox="0 0 10 10" aria-label="fax"><rect x="2.5" y="0.5" width="5" height="2.5"/><rect x="0.5" y="3.5" width="9" height="4" rx="1"/><rect x="2.5" y="6.5" width="5" height="3"/></svg></li>
    <li>info@marlowurban.com
      <svg viewBox="0 0 10 10" aria-label="email"><path d="M0.5,2 H9.5 V8.5 H0.5 Z M1.5,3 V7.5 H8.5 V3 L5,5.6 Z M2,3 L5,5 L8,3 Z" fill-rule="evenodd"/></svg></li>
    <li>www.marlowurban.com
      <svg viewBox="0 0 10 10" aria-label="website"><circle cx="5" cy="5" r="4.2" fill="none" stroke="var(--brand-blue)" stroke-width="1"/><ellipse cx="5" cy="5" rx="1.8" ry="4.2" fill="none" stroke="var(--brand-blue)" stroke-width="0.8"/><path d="M1,5 H9" stroke="var(--brand-blue)" stroke-width="0.8"/></svg></li>
  </ul>
  <div class="header-rule"></div>
  <p class="footer-address">2275 E, Halvorsen Ave., Brinley, WA 99318</p>
</section>

</body>
</html>
```